Make a high end Clubcard for personal training studio. Not a business card but a clubcard

Important! Not a business card buT a clubcard

I need club cards for my clients to check in. My personal training studio is a high end studio with high prices so it needs to look classy and expensive.

You can use the attachment that you like.

the website url needs to be on the card www.Vornikfit.nl

The card needs to have 2 way design.

I will choose the best Design and have more projects for the winner

Place the following text on the one side of the card:

Personal Training Studio Brekeveld

personal training and fitness

Fitness

53,9 x 85,7mm

• Classy and expensive
• Classy and expensive

```html
<!DOCTYPE html>
<html lang="en">
<head>
<meta charset="utf-8">
<title>Vornikfit Clubcard</title>
<link rel="stylesheet" href="https://fonts.googleapis.com/css2?family=Roboto+Slab:wght@300;400;700&family=Open+Sans:wght@300;400&display=swap">
<style>
  :root {
    --page: #e8e6e3;
    --card-light: #fbfbfb;
    --card-mid: #e6e6e6;
    --red: #d6262e;
    --red-dark: #a8121a;
    --red-deep: #7d0b10;
    --grey-band: #c9c9c9;
    --grey-band-dark: #9d9d9d;
    --text-soft: #b9b9b9;
    --text-mid: #a6a6a6;
    --ink: #1b1b1b;
  }
  * { margin: 0; padding: 0; box-sizing: border-box; }
  html, body { width: 1200px; height: 1023px; overflow: hidden; }
  body {
    background: var(--page);
    position: relative;
    font-family: "Open Sans", sans-serif;
  }
  .card {
    position: absolute;
    left: 220px;
    width: 760px;
    height: 478px;
    overflow: hidden;
    border-radius: 4px;
    box-shadow: 0 6px 18px rgba(0,0,0,.18);
  }
  .card--front { top: 18px; }
  .card--back { top: 527px; }
  .card__surface {
    position: absolute; inset: 0;
    background:
      linear-gradient(155deg, var(--card-light) 0%, #f1f1f1 40%, var(--card-mid) 70%, #f4f4f4 100%);
  }
  .card__bands { position: absolute; inset: 0; }
  .brand {
    position: absolute;
    display: flex;
    align-items: center;
    gap: 14px;
  }
  .brand__mark {
    width: 54px; height: 54px;
    border-radius: 50%;
    background: var(--red);
    border: 4px solid var(--ink);
    flex: none;
  }
  .brand__name {
    font-family: "Roboto Slab", serif;
    font-weight: 700;
    font-size: 40px;
    line-height: 1;
    color: var(--red);
  }
  .brand__line {
    font-family: "Roboto Slab", serif;
    font-weight: 700;
    font-size: 25px;
    line-height: 1.1;
    color: var(--ink);
  }
  .brand__tagline {
    font-family: "Roboto Slab", serif;
    font-size: 9.5px;
    letter-spacing: .8px;
    color: var(--ink);
    margin-top: 3px;
    white-space: nowrap;
  }
  .card--front .brand { left: 330px; top: 42px; }
  .card--back .brand { left: 360px; top: 150px; }
  .member {
    position: absolute;
    left: 150px; top: 210px;
    font-weight: 300;
    font-size: 36px;
    line-height: 1.15;
    color: var(--text-soft);
  }
  .clubcard {
    position: absolute;
    left: 178px; top: 305px;
  }
  .clubcard__title {
    font-family: "Roboto Slab", serif;
    font-weight: 400;
    font-size: 108px;
    line-height: 1;
    color: var(--text-mid);
    letter-spacing: -1px;
  }
  .clubcard__studio {
    font-family: "Roboto Slab", serif;
    font-weight: 300;
    font-size: 21px;
    color: var(--text-mid);
    margin-top: 4px;
    letter-spacing: .5px;
    white-space: nowrap;
  }
  .clubcard__url {
    font-family: "Roboto Slab", serif;
    font-weight: 300;
    font-size: 21px;
    color: var(--red);
    letter-spacing: .5px;
  }
</style>
</head>
<body>

  <section class="card card--front" aria-label="Clubcard front">
    <div class="card__surface"></div>
    <svg class="card__bands" viewBox="0 0 760 478" aria-hidden="true">
      <polygon points="0,300 46,300 150,478 0,478" fill="var(--grey-band)"/>
      <polygon points="0,330 30,330 118,478 0,478" fill="var(--red)"/>
      <polygon points="0,380 14,380 72,478 0,478" fill="var(--red-dark)"/>
      <polygon points="60,478 85,440 120,478" fill="var(--red-deep)"/>
      <polygon points="620,0 760,0 760,170 700,170" fill="var(--grey-band)"/>
      <polygon points="660,0 760,0 760,300 735,300" fill="var(--red)"/>
      <polygon points="705,0 760,0 760,90" fill="var(--red-dark)"/>
      <polygon points="680,110 760,110 760,190" fill="var(--red-deep)"/>
      <polygon points="735,300 760,300 760,478 752,478" fill="var(--grey-band-dark)"/>
    </svg>
    <div class="brand">
      <span class="brand__mark"></span>
      <div>
        <div class="brand__name">Vornikfit</div>
        <div class="brand__line">Personal training</div>
        <div class="brand__tagline">STRONGER WITH EVERY SESSION</div>
      </div>
    </div>
    <div class="member">
      <div>John Doe</div>
      <div>123.456.789.11</div>
    </div>
    <div class="clubcard">
      <div class="clubcard__title">Clubcard</div>
      <div class="clubcard__studio">Personal Training Studio Brekeveld</div>
      <div class="clubcard__url">www.Vornikfit.nl</div>
    </div>
  </section>

  <section class="card card--back" aria-label="Clubcard back">
    <div class="card__surface"></div>
    <svg class="card__bands" viewBox="0 0 760 478" aria-hidden="true">
      <polygon points="0,0 110,0 40,120 0,120" fill="var(--grey-band)"/>
      <polygon points="0,0 60,0 0,95" fill="var(--grey-band-dark)"/>
      <polygon points="0,360 130,360 200,410 760,410 760,478 0,478" fill="var(--red)"/>
      <polygon points="0,360 95,360 150,400 0,400" fill="var(--red-deep)"/>
      <polygon points="200,440 760,420 760,478 180,478" fill="var(--red-dark)"/>
      <polygon points="0,420 200,420 230,478 0,478" fill="var(--red-dark)"/>
    </svg>
    <div class="brand">
      <span class="brand__mark"></span>
      <div>
        <div class="brand__name">Vornikfit</div>
        <div class="brand__line">Personal training</div>
        <div class="brand__tagline">STRONGER WITH EVERY SESSION</div>
      </div>
    </div>
  </section>

</body>
</html>
```